Simple and Clean business card design

We would like the design to be simple clean and to incorporate our colors.

We are open to your design and talent, we have the dots in our logo as we think of it as data points and we connect data points for people.

We are open to see the great creative and clean design you bring to the table

Contact Information for Business Card

please include: name, position, email, phone and website

Font styles to use
Sans Serif

Requirements
Must have
• my colors incorporated, simplicity
Nice to have
• lots of white space, simplicity
Should not have
• complexicity/ complex art

```html
<!DOCTYPE html>
<html lang="en">
<head>
<meta charset="utf-8">
<title>Driftly Business Card</title>
<link rel="stylesheet" href="https://fonts.googleapis.com/css2?family=Montserrat:wght@500;600;700&family=Arimo:wght@400&display=swap">
<style>
  :root {
    --bg: #2b2b2b;
    --card-dark: #0e0e0e;
    --card-light: #ffffff;
    --ink: #111111;
    --blue: #4285f4;
    --green: #34a853;
    --yellow: #fbbc05;
    --red: #ea4335;
    --rule: #8a8a8a;
  }
  * { box-sizing: border-box; margin: 0; padding: 0; }
  html, body { width: 1200px; height: 1040px; overflow: hidden; }
  body {
    background: var(--bg);
    display: flex;
    flex-direction: column;
    align-items: center;
    justify-content: center;
    gap: 56px;
  }
  .card {
    width: 640px;
    height: 366px;
    position: relative;
  }
  .card--back {
    background: var(--card-dark);
    border-radius: 90px 0 90px 0;
    display: flex;
    align-items: center;
    justify-content: center;
  }
  .card--front {
    background: var(--card-light);
    border-radius: 0 90px 0 90px;
    display: flex;
    align-items: center;
  }
  .wordmark {
    display: flex;
    align-items: center;
    gap: 14px;
    font-family: "Montserrat", sans-serif;
    font-weight: 600;
    letter-spacing: 1px;
  }
  .wordmark__dot {
    width: 22px;
    height: 22px;
    border-radius: 50%;
    background: var(--blue);
  }
  .card--back .wordmark { font-size: 78px; color: #ffffff; }
  .card--front .wordmark { font-size: 62px; color: var(--ink); }
  .front__brand {
    width: 320px;
    display: flex;
    justify-content: center;
  }
  .front__divider {
    width: 1px;
    height: 230px;
    background: var(--rule);
  }
  .front__details {
    padding-left: 28px;
    font-family: "Arimo", sans-serif;
    color: var(--ink);
  }
  .person__name {
    font-family: "Montserrat", sans-serif;
    font-weight: 700;
    font-size: 27px;
    line-height: 1;
  }
  .person__role {
    font-size: 18px;
    color: var(--blue);
    margin-top: 4px;
  }
  .contact-list {
    list-style: none;
    margin-top: 34px;
    display: flex;
    flex-direction: column;
    gap: 8px;
  }
  .contact-list__item {
    display: flex;
    align-items: center;
    gap: 10px;
    font-size: 18px;
  }
  .contact-list__icon {
    width: 24px;
    height: 24px;
    flex: none;
  }
  .contact-list__highlight { color: var(--blue); }
</style>
</head>
<body>
  <section class="card card--back">
    <div class="wordmark"><span class="wordmark__dot"></span>Driftly</div>
  </section>

  <section class="card card--front">
    <div class="front__brand">
      <div class="wordmark"><span class="wordmark__dot"></span>Driftly</div>
    </div>
    <div class="front__divider"></div>
    <div class="front__details">
      <p class="person__name">Owen Lacroix</p>
      <p class="person__role">Founder/ CEO</p>
      <ul class="contact-list">
        <li class="contact-list__item">
          <svg class="contact-list__icon" viewBox="0 0 24 24" aria-hidden="true">
            <circle cx="12" cy="12" r="12" fill="var(--green)"/>
            <path d="M8.5 6.5l2 2.2-1.2 1.4c.8 1.7 2 2.9 3.6 3.7l1.4-1.2 2.2 2-1.2 1.8c-4.2-.4-8.1-4.3-8.5-8.5z" fill="#fff"/>
          </svg>
          555-204-7816
        </li>
        <li class="contact-list__item">
          <svg class="contact-list__icon" viewBox="0 0 24 24" aria-hidden="true">
            <circle cx="12" cy="12" r="12" fill="var(--yellow)"/>
            <rect x="6" y="8" width="12" height="8.5" fill="none" stroke="#fff" stroke-width="1.4"/>
            <path d="M6 8l6 5 6-5" fill="none" stroke="#fff" stroke-width="1.4"/>
          </svg>
          owen.lacroix@driftly.one
        </li>
        <li class="contact-list__item">
          <svg class="contact-list__icon" viewBox="0 0 24 24" aria-hidden="true">
            <circle cx="12" cy="12" r="12" fill="var(--red)"/>
            <circle cx="12" cy="12" r="6" fill="none" stroke="#fff" stroke-width="1.3"/>
            <ellipse cx="12" cy="12" rx="2.6" ry="6" fill="none" stroke="#fff" stroke-width="1.1"/>
            <path d="M6 12h12M7 9h10M7 15h10" stroke="#fff" stroke-width="1.1"/>
          </svg>
          <span>www.<span class="contact-list__highlight">Driftly</span>.one</span>
        </li>
      </ul>
    </div>
  </section>
</body>
</html>
```